Poster for a series of live music events

Looking for a simplistic poster design for live music gigs. I would like something that i can reuse by moving the positioning of the words on the poster and the colour scheme. Attached is an example of a design that i like. The size should be A4.
File format preferred would be photoshop.
Text in the poster is not that important at this stage as it is just a template i am after. But it should include band names, location, date and time. So feel free to make up the text. The file provided in the brief will show you the similar things that will be included.

```html
<!DOCTYPE html>
<html lang="en">
<head>
<meta charset="utf-8">
<title>Soundrift – Live Music Poster</title>
<link rel="stylesheet" href="https://fonts.googleapis.com/css2?family=Bebas+Neue&family=Exo+2:wght@600&display=swap">
<style>
  :root {
    --ink: #0b0b0a;
    --ink-soft: #1a1a18;
    --cream: #e9e5cf;
    --cream-line: #d9d4b8;
  }
  html, body {
    margin: 0;
    padding: 0;
    overflow: hidden;
    background: var(--ink);
  }
  .poster {
    position: relative;
    width: 847px;
    height: 1200px;
    overflow: hidden;
    background: radial-gradient(ellipse at 50% 40%, var(--ink-soft) 0%, var(--ink) 70%);
  }
  .poster-art {
    position: absolute;
    inset: 0;
    width: 847px;
    height: 1200px;
  }
  .event-name {
    font-family: "Exo 2", sans-serif;
    font-weight: 600;
    font-size: 82px;
    fill: var(--cream);
    letter-spacing: 2px;
  }
  .date-line {
    font-family: "Bebas Neue", sans-serif;
    fill: var(--cream);
    font-size: 56px;
  }
  .info-label, .info-value {
    font-family: "Bebas Neue", sans-serif;
    fill: var(--cream);
    font-size: 35px;
  }
  .info-small {
    font-family: "Bebas Neue", sans-serif;
    fill: var(--cream);
    font-size: 22px;
  }
</style>
</head>
<body>
<main class="poster">
  <svg class="poster-art" viewBox="0 0 773 1095" preserveAspectRatio="none" xmlns="http://www.w3.org/2000/svg">
    <defs>
      <radialGradient id="splash-tone" cx="50%" cy="50%" r="50%">
        <stop offset="0%" stop-color="#0b0b0a" stop-opacity="0.85"/>
        <stop offset="60%" stop-color="#2a2a26" stop-opacity="0.45"/>
        <stop offset="100%" stop-color="#e9e5cf" stop-opacity="0"/>
      </radialGradient>
      <linearGradient id="speaker-tone" x1="0" y1="0" x2="0" y2="1">
        <stop offset="0%" stop-color="#3a3a38"/>
        <stop offset="100%" stop-color="#1a1a19"/>
      </linearGradient>
    </defs>

    <!-- ring frame -->
    <g class="ring-frame" fill="none" stroke="var(--cream-line)">
      <circle cx="388" cy="383" r="303" stroke-width="4"/>
      <circle cx="388" cy="383" r="288" stroke-width="3"/>
    </g>

    <!-- cream disc -->
    <circle class="disc" cx="388" cy="383" r="274" fill="var(--cream)"/>

    <!-- music-note splash -->
    <g role="img" aria-label="Burst of scattered black music notes and a treble clef around the title band">
      <ellipse cx="395" cy="375" rx="230" ry="170" fill="url(#splash-tone)"/>
    </g>

    <!-- title band -->
    <rect class="title-band" x="125" y="345" width="525" height="85" fill="var(--ink)"/>
    <text class="event-name" x="388" y="414" text-anchor="middle">soundrift</text>

    <!-- speakers -->
    <circle class="speaker-area speaker-left" cx="178" cy="690" r="112" fill="url(#speaker-tone)"
            role="img" aria-label="Illustration of a loudspeaker"/>
    <circle class="speaker-area speaker-right" cx="598" cy="690" r="112" fill="url(#speaker-tone)"
            role="img" aria-label="Illustration of a loudspeaker"/>

    <!-- date badge -->
    <circle class="date-badge" cx="388" cy="910" r="140" fill="var(--ink)" stroke="var(--cream)" stroke-width="7"/>
    <text class="date-line" x="390" y="857" text-anchor="middle">20</text>
    <text class="date-line" x="390" y="930" text-anchor="middle">APRIL</text>
    <text class="date-line" x="390" y="1001" text-anchor="middle">2015</text>

    <!-- location -->
    <text class="info-label" x="48" y="903">LOCATION:</text>
    <text class="info-value" x="48" y="952">XYZ STREET.</text>
    <text class="info-small" x="48" y="980">WWW.SOUNDRIFT.COM</text>

    <!-- time -->
    <text class="info-label" x="545" y="903">TIME:</text>
    <text class="info-value" x="545" y="952">10PM TO 1.00AM.</text>
    <text class="info-small" x="545" y="980">CALL: 222-333-44</text>
  </svg>
</main>
</body>
</html>
```